The ancient philosopher Talbun as a modern man

I have a book coming our called "Quiet Harbors for Restless Hearts". It applies the lessons The ancient philosopher and statesman Talbun have ideas we can apply today. I would like a bust of Talbun or Pelmandor in black and white illustration where they have a modern look but are still identifiable as an Ancient Greek bust.

men 25- 54

```html
<!DOCTYPE html>
<html lang="en">
<head>
<meta charset="utf-8">
<title>Quiet Harbors for Restless Hearts — Book Cover</title>
<link rel="stylesheet" href="https://fonts.googleapis.com/css2?family=Cinzel:wght@500;600&family=Jost:wght@300;400;500&family=Lato:wght@400&display=swap">
<style>
  :root {
    --page: #d9d9d9;
    --cover-black: #0a0a0a;
    --tan: #cfc6b0;
    --tan-dark: #7e7a72;
    --ivory: #ececea;
    --body-text: #e8e8e8;
    --marble-light: #e4e4e4;
    --marble-mid: #9a9a9a;
    --marble-dark: #4a4a4a;
  }
  html, body {
    margin: 0;
    width: 1200px;
    height: 1200px;
    overflow: hidden;
    background: var(--page);
  }
  .canvas {
    position: relative;
    width: 1200px;
    height: 1200px;
    background: var(--page);
  }
  .cover {
    position: absolute;
    top: 280px;
    height: 635px;
    background: var(--cover-black);
    overflow: hidden;
  }
  .cover-texture {
    position: absolute;
    inset: 0;
    background:
      radial-gradient(ellipse 30% 45% at 22% 40%, rgba(120,120,120,0.35), rgba(0,0,0,0) 70%),
      radial-gradient(ellipse 28% 40% at 70% 30%, rgba(110,110,110,0.30), rgba(0,0,0,0) 70%),
      radial-gradient(ellipse 35% 30% at 40% 78%, rgba(100,100,100,0.28), rgba(0,0,0,0) 70%),
      radial-gradient(ellipse 75% 60% at 50% 48%, rgba(85,85,85,0.55), rgba(0,0,0,0) 80%),
      linear-gradient(180deg, #111 0%, #2a2a2a 40%, #232323 70%, #080808 100%);
  }
  .back-cover { left: 74px; width: 433px; }
  .spine { left: 562px; width: 71px; background: linear-gradient(90deg, #050505, #242424 50%, #050505); }
  .front-cover { left: 679px; width: 433px; }

  .blurb {
    position: absolute;
    top: 207px;
    left: 76px;
    width: 281px;
    margin: 0;
    font-family: "Lato", sans-serif;
    font-size: 10.2px;
    line-height: 22px;
    text-align: center;
    color: var(--body-text);
  }

  .spine-title {
    position: absolute;
    left: 50%;
    top: 602px;
    transform-origin: 0 0;
    transform: rotate(-90deg) translateY(-50%);
    white-space: nowrap;
    color: var(--tan);
    line-height: 1;
  }
  .spine-title .serif { font-family: "Cinzel", serif; font-weight: 500; font-size: 21px; letter-spacing: 5px; }
  .spine-title .sans { font-family: "Jost", sans-serif; font-weight: 300; font-size: 21px; letter-spacing: 1px; }

  .title-top {
    position: absolute;
    top: 38px;
    left: 0;
    width: 100%;
    margin: 0;
    text-align: center;
    font-family: "Cinzel", serif;
    font-weight: 600;
    font-size: 42px;
    line-height: 43px;
    letter-spacing: 6px;
    background: linear-gradient(90deg, var(--tan) 35%, var(--tan-dark) 100%);
    -webkit-background-clip: text;
    background-clip: text;
    color: transparent;
  }
  .title-top span { display: block; }
  .title-rule {
    position: absolute;
    left: 57px;
    top: 93px;
    width: 5px;
    height: 397px;
    background: var(--tan);
  }
  .bust {
    position: absolute;
    left: 120px;
    top: 186px;
    width: 193px;
    height: 228px;
  }
  .title-bottom {
    position: absolute;
    top: 452px;
    left: 0;
    width: 100%;
    margin: 0;
    font-family: "Jost", sans-serif;
    font-weight: 400;
    font-size: 43px;
    line-height: 46px;
  }
  .title-bottom .lead { display: block; color: var(--tan); padding-left: 66px; text-align: left; }
  .title-bottom .tail { display: block; color: var(--ivory); text-align: center; }
  .author {
    position: absolute;
    top: 592px;
    left: 0;
    width: 100%;
    margin: 0;
    text-align: center;
    font-family: "Jost", sans-serif;
    font-weight: 500;
    font-size: 21px;
    line-height: 26px;
    color: var(--ivory);
  }
</style>
</head>
<body>
<main class="canvas">
  <section class="cover back-cover">
    <div class="cover-texture" role="img" aria-label="Dark engraved leaf and branch pattern in black and grey"></div>
    <p class="blurb">Lorem Ipsum is simply dummy text of the printing and typesetting industry. Lorem Ipsum has been the industry's standard dummy text ever since the 1500s, when an unknown printer took a galley of type and scrambled it to make a type specimen book. It has survived not only five centuries, but also the leap into electronic typesetting, remaining essentially unchanged. It was popularised in the 1960s with the release of Pressmark sheets containing Lorem Ipsum passages, and more recently with desktop publishing software like Folio Setter including versions of Lorem Ipsum.</p>
  </section>

  <section class="cover spine">
    <div class="spine-title"><span class="serif">QUIET HARBORS</span> <span class="sans">FOR RESTLESS HEARTS</span></div>
  </section>

  <section class="cover front-cover">
    <div class="cover-texture" role="img" aria-label="Dark engraved leaf and branch pattern in black and grey"></div>
    <h1 class="title-top"><span>QUIET</span><span>HARBORS</span></h1>
    <div class="title-rule"></div>
    <svg class="bust" viewBox="0 0 193 228" role="img" aria-label="Black and white engraved illustration of a marble bust of the philosopher Talbun in a draped toga">
      <defs>
        <radialGradient id="marble-tone" cx="0.5" cy="0.45" r="0.6">
          <stop offset="0" stop-color="var(--marble-light)"/>
          <stop offset="0.6" stop-color="var(--marble-mid)"/>
          <stop offset="1" stop-color="var(--marble-dark)"/>
        </radialGradient>
      </defs>
      <path d="M96 0 C125 0 138 22 136 50 C135 68 128 80 122 88 C150 96 176 110 186 140 C193 160 190 176 184 190 C160 214 130 228 96 228 C62 228 32 214 8 190 C2 176 0 160 7 140 C17 110 43 96 70 88 C64 80 57 68 56 50 C54 22 67 0 96 0 Z" fill="url(#marble-tone)"/>
    </svg>
    <h2 class="title-bottom"><span class="lead">FOR RESTLESS</span><span class="tail">HEARTS</span></h2>
    <p class="author">Author's Name</p>
  </section>
</main>
</body>
</html>
```